Quiet Fern Acupuncture
Quiet Fern Acupuncture -
Creative Brief
Bright & Fun-filled
Marla Pennick-Vasquez
LAc, Dipl, Ac
2730 N Ridley Avenue, Suite 410 Flagstaff, AZ, 86044 @ Haverstock Chiropractic
quietfernacupuncture@mailbox-example.com
an appointment reminder card

```html
<!DOCTYPE html>
<html lang="en">
<head>
<meta charset="utf-8">
<title>Quiet Fern Acupuncture – Stationery</title>
<link rel="stylesheet" href="https://fonts.googleapis.com/css2?family=Raleway:wght@300;400;600&display=swap">
<style>
  :root{
    --backdrop:#2a2a2c;
    --paper:#ffffff;
    --paper-shade:#eeeeee;
    --ink:#4a4a4a;
    --ink-soft:#8a8a8a;
    --accent-orange:#f08a1e;
    --wave-red:#e2312b;
    --wave-yellow:#f7b51c;
    --wave-blue:#2b8fd6;
    --wave-grey:#d9d9d9;
    --faint-peach:#fbe6d8;
    --faint-lilac:#efe4f1;
    --rule:#c9c9c9;
  }
  *{box-sizing:border-box;margin:0;padding:0}
  html,body{width:1200px;height:768px;overflow:hidden}
  body{background:var(--backdrop);font-family:"Raleway",sans-serif;color:var(--ink);position:relative}
  .sheet{position:absolute;background:var(--paper);overflow:hidden;box-shadow:0 2px 6px rgba(0,0,0,.45)}
  .card-front{left:72px;top:43px;width:245px;height:132px;border-radius:6px}
  .card-back{left:336px;top:43px;width:240px;height:132px;border-radius:6px}
  .envelope{left:72px;top:202px;width:504px;height:146px}
  .notecard{left:72px;top:396px;width:504px;height:324px}
  .letterhead{left:660px;top:43px;width:468px;height:677px}

  .brand{display:flex;flex-direction:column;align-items:flex-start}
  .brand-dot{border-radius:50%;background:var(--accent-orange)}
  .brand-name{font-weight:400;color:var(--ink);line-height:1.05}

  .waves{position:absolute;left:0;bottom:0;width:100%}

  /* business card */
  .card-front .brand{position:absolute;left:14px;top:18px}
  .card-front .brand-dot{width:30px;height:30px;margin:0 0 4px 8px}
  .card-front .brand-name{font-size:11px;width:80px}
  .card-details{position:absolute;left:104px;top:18px;font-size:5.6px;line-height:1.5;color:var(--ink-soft)}
  .card-details .person{color:var(--accent-orange);font-weight:600;font-size:6.4px}
  .card-details .creds{color:var(--accent-orange);margin-bottom:6px}
  .card-front .waves{height:34px}

  /* reminder card */
  .reminder-title{position:absolute;left:14px;top:12px;font-size:7px;font-weight:600}
  .reminder-rows{position:absolute;left:14px;top:28px;right:14px;font-size:6px;color:var(--ink-soft)}
  .reminder-row{display:flex;gap:10px;margin-bottom:7px}
  .reminder-row span{flex:1;border-bottom:1px solid var(--rule);padding-bottom:1px}
  .card-back .waves{height:30px}

  /* envelope */
  .return-address{position:absolute;left:0;right:0;top:14px;text-align:center;font-size:6px;line-height:1.5;color:var(--ink-soft)}
  .envelope-flap{position:absolute;left:0;right:0;top:0;height:5px;background:var(--paper-shade)}

  /* notecard */
  .notecard .brand{position:absolute;left:22px;top:50px}
  .notecard .brand-dot{width:48px;height:48px;margin:0 0 6px 6px}
  .notecard .brand-name{font-size:19px;width:150px}
  .faint-mark{position:absolute;border-radius:50%;background:radial-gradient(circle at 40% 40%,var(--faint-peach),var(--faint-lilac) 70%,#f6f0f4)}
  .notecard .faint-mark{left:300px;top:14px;width:150px;height:150px;opacity:.7}
  .notecard .waves{height:110px}

  /* letterhead */
  .letterhead .brand{position:absolute;left:150px;top:36px}
  .letterhead .brand-dot{width:42px;height:42px;margin:0 0 6px 4px}
  .letterhead .brand-name{font-size:17px;width:140px}
  .letterhead .faint-mark{left:150px;top:236px;width:190px;height:190px;opacity:.75}
  .letter-footer{position:absolute;right:22px;bottom:104px;font-size:6.6px;line-height:1.55;color:var(--ink-soft);text-align:left}
  .letterhead .waves{height:90px}
</style>
</head>
<body>

<section class="sheet card-front">
  <div class="brand">
    <div class="brand-dot"></div>
    <div class="brand-name">Quiet Fern Acupuncture</div>
  </div>
  <div class="card-details">
    <div class="person">Marla Pennick-Vasquez</div>
    <div class="creds">LAc, Dipl, Ac</div>
    <div>2730 N Ridley Avenue, Suite 410</div>
    <div>Flagstaff, AZ 86044</div>
    <div>@ Haverstock Chiropractic</div>
    <div>quietfernacupuncture@mailbox-example.com</div>
  </div>
  <svg class="waves" viewBox="0 0 245 34" preserveAspectRatio="none">
    <path d="M0 34 L0 24 Q120 6 245 16 L245 34 Z" fill="var(--wave-grey)" opacity=".45"/>
    <path d="M0 26 Q40 20 80 20" fill="none" stroke="var(--wave-red)" stroke-width="3"/>
    <path d="M80 20 Q130 18 175 16" fill="none" stroke="var(--wave-yellow)" stroke-width="3"/>
    <path d="M175 16 Q215 12 245 13" fill="none" stroke="var(--wave-blue)" stroke-width="3"/>
  </svg>
</section>

<section class="sheet card-back">
  <div class="reminder-title">Your Next Appointment is on:</div>
  <div class="reminder-rows">
    <div class="reminder-row"><span>Date:</span><span>Time:</span></div>
    <div class="reminder-row"><span>Date:</span><span>Time:</span></div>
    <div class="reminder-row"><span>Date:</span><span>Time:</span></div>
  </div>
  <svg class="waves" viewBox="0 0 240 30" preserveAspectRatio="none">
    <path d="M0 30 L0 22 Q120 6 240 14 L240 30 Z" fill="var(--wave-grey)" opacity=".45"/>
    <path d="M0 24 Q40 18 78 18" fill="none" stroke="var(--wave-red)" stroke-width="3"/>
    <path d="M78 18 Q125 16 170 14" fill="none" stroke="var(--wave-yellow)" stroke-width="3"/>
    <path d="M170 14 Q210 10 240 11" fill="none" stroke="var(--wave-blue)" stroke-width="3"/>
  </svg>
</section>

<section class="sheet envelope">
  <div class="envelope-flap"></div>
  <div class="return-address">
    <div>2730 N Ridley Avenue, Suite 410</div>
    <div>Flagstaff, AZ 86044</div>
    <div>@ Haverstock Chiropractic</div>
  </div>
</section>

<section class="sheet notecard">
  <div class="faint-mark" role="img" aria-label="Faint soft circular background tint"></div>
  <div class="brand">
    <div class="brand-dot"></div>
    <div class="brand-name">Quiet Fern Acupuncture</div>
  </div>
  <svg class="waves" viewBox="0 0 504 110" preserveAspectRatio="none">
    <path d="M0 110 L0 78 Q250 20 504 44 L504 110 Z" fill="var(--wave-grey)" opacity=".4"/>
    <path d="M0 86 Q70 70 150 62" fill="none" stroke="var(--wave-red)" stroke-width="7"/>
    <path d="M150 62 Q260 50 360 46" fill="none" stroke="var(--wave-yellow)" stroke-width="7"/>
    <path d="M360 46 Q440 40 504 44" fill="none" stroke="var(--wave-blue)" stroke-width="7"/>
  </svg>
</section>

<section class="sheet letterhead">
  <div class="brand">
    <div class="brand-dot"></div>
    <div class="brand-name">Quiet Fern Acupuncture</div>
  </div>
  <div class="faint-mark" role="img" aria-label="Faint soft circular background tint"></div>
  <div class="letter-footer">
    <div>2730 N Ridley Avenue, Suite 410</div>
    <div>Flagstaff, AZ 86044</div>
    <div>@ Haverstock Chiropractic</div>
    <div>quietfernacupuncture@mailbox-example.com</div>
  </div>
  <svg class="waves" viewBox="0 0 468 90" preserveAspectRatio="none">
    <path d="M0 90 L0 62 Q230 20 468 30 L468 90 Z" fill="var(--wave-grey)" opacity=".4"/>
    <path d="M0 68 Q70 52 150 46" fill="none" stroke="var(--wave-red)" stroke-width="6"/>
    <path d="M150 46 Q250 36 340 32" fill="none" stroke="var(--wave-yellow)" stroke-width="6"/>
    <path d="M340 32 Q410 26 468 30" fill="none" stroke="var(--wave-blue)" stroke-width="6"/>
  </svg>
</section>

</body>
</html>
```